FAST TURN AROUND - Yoga & Sound Meditation Event Flyer

Our organization - Tarrow Guidance Alliance - is currently looking for someone to create a flyer for an upcoming Yoga & Sound Meditation Event.

We are looking for the following deliverables:
Versions of the Flyer created for Social Media (Long Story & Square Post) that includes the following information. (Not including the categories)
Event Title: Tarrow Flow & Hum Unwind Session - Bayline Mix
Event Date & Time: Wednesday, April 20 | 7P - 9P
Event Location: Reedhall at Cobbleyard
Tarrow Logo: (Both black and white versions are attached. Feel free to use whichever makes more sense based on the lighting)

We would want a version of this for the eight different background images provided. For the test, you can submit 1-2 since the rest of the details will be the same once we chose the information design.

```html
<!DOCTYPE html>
<html lang="en">
<head>
<meta charset="utf-8">
<title>Tarrow Flow &amp; Hum Unwind Session – Square Post</title>
<link rel="stylesheet" href="https://fonts.googleapis.com/css2?family=Bebas+Neue&family=Open+Sans:wght@400;600&family=Poppins:wght@400;600;700&display=swap">
<style>
  :root {
    --page-bg: #ececec;
    --paper: #ffffff;
    --ink: #1b1b1b;
    --red: #e8342b;
    --orange: #f39322;
    --orange-deep: #ea5a20;
    --brush-a: #f26a22;
    --brush-b: #f79a26;
    --photo-dark: #231b18;
    --photo-mid: #5b4c45;
    --photo-light: #8f8580;
  }
  * { box-sizing: border-box; margin: 0; padding: 0; }
  html, body {
    width: 960px; height: 1200px; overflow: hidden;
    background: var(--page-bg);
  }
  .post {
    position: absolute; left: 0; top: 120px;
    width: 960px; height: 960px;
    background: var(--paper);
    overflow: hidden;
  }
  .post-art { position: absolute; inset: 0; width: 960px; height: 960px; }

  .brand { position: absolute; left: 250px; top: 70px; }
  .brand-name {
    font-family: "Poppins", sans-serif; font-weight: 700;
    font-size: 74px; line-height: 1; letter-spacing: -1px;
    color: var(--ink);
  }
  .brand-tagline {
    font-family: "Open Sans", sans-serif; font-weight: 400;
    font-size: 25px; color: var(--ink); margin-top: 2px;
  }

  .event-title {
    position: absolute; left: 470px; width: 460px; top: 262px;
    text-align: center;
    font-family: "Bebas Neue", sans-serif; font-weight: 400;
    font-size: 86px; line-height: 92px;
    text-shadow: 0 0 6px #fff, 0 0 2px #fff;
  }
  .event-title span { display: block; white-space: nowrap; }
  .title-red { color: var(--red); }
  .title-orange { color: var(--orange); }
  .title-ink { color: var(--ink); }

  .event-when {
    position: absolute; left: 510px; width: 380px; top: 686px;
    text-align: center; isolation: isolate;
  }
  .event-when-label {
    font-family: "Bebas Neue", sans-serif; font-size: 36px;
    color: var(--ink); line-height: 1;
  }
  .brush {
    position: relative; display: inline-block; z-index: 1;
    font-family: "Poppins", sans-serif; font-weight: 600;
    font-size: 30px; line-height: 44px; color: #fff;
    padding: 0 26px;
  }
  .brush::before {
    content: ""; position: absolute; inset: 2px 0; z-index: -1;
    border-radius: 3px;
  }
  .brush-day { margin-top: 8px; }
  .brush-day::before { background: var(--brush-a); transform: skewX(-8deg); }
  .brush-date { padding: 0 28px; }
  .brush-date::before { background: var(--brush-b); transform: skewX(6deg); }

  .event-where {
    position: absolute; left: 460px; width: 420px; top: 878px;
    text-align: center; color: #fff; font-family: "Poppins", sans-serif;
  }
  .event-where-label { font-size: 26px; font-weight: 400; line-height: 32px; }
  .event-where-venue { font-size: 33px; font-weight: 700; line-height: 40px; white-space: nowrap; }
</style>
</head>
<body>
<main class="post">
  <svg class="post-art" viewBox="0 0 960 960">
    <defs>
      <linearGradient id="photoTone" x1="0" y1="0" x2="1" y2="1">
        <stop offset="0" stop-color="var(--photo-light)"/>
        <stop offset="0.35" stop-color="var(--photo-mid)"/>
        <stop offset="1" stop-color="var(--photo-dark)"/>
      </linearGradient>
      <linearGradient id="topBand" x1="0" y1="0" x2="1" y2="0">
        <stop offset="0" stop-color="#f7a126"/>
        <stop offset="1" stop-color="#e9872a"/>
      </linearGradient>
      <linearGradient id="bottomBand" x1="0" y1="0" x2="1" y2="0">
        <stop offset="0" stop-color="#f17a22"/>
        <stop offset="1" stop-color="#e84a1f"/>
      </linearGradient>
    </defs>

    <path role="img" aria-label="Photo of a woman in glasses meditating with hands pressed together"
      fill="url(#photoTone)"
      d="M0,95 C40,70 120,62 170,110 C230,170 255,230 320,262 C400,302 430,380 470,460 C510,540 520,620 540,700 C560,780 520,870 500,960 L0,960 Z"/>

    <path class="corner-arc" fill="var(--orange-deep)" d="M0,0 L135,0 A135,135 0 0 1 0,125 Z"/>
    <g fill="none" stroke="#ffffff" stroke-width="2" opacity="0.85">
      <path d="M0,40 A95,95 0 0 0 95,0"/>
      <path d="M0,80 A125,125 0 0 0 125,0"/>
    </g>
    <g fill="none" stroke="#d9d9d9" stroke-width="1.5">
      <path d="M150,0 C200,120 300,200 380,280 C460,360 500,500 540,640"/>
      <path d="M190,0 C240,110 340,190 420,270 C500,350 540,490 580,630"/>
    </g>

    <path class="top-band" fill="url(#topBand)"
      d="M462,0 L960,0 L960,142 C915,150 870,120 820,96 C770,78 745,138 702,132 C660,124 650,62 600,38 C560,20 510,12 462,0 Z"/>

    <path class="bottom-band" fill="url(#bottomBand)"
      d="M380,960 C410,905 470,872 560,868 C640,866 690,896 770,886 C840,878 880,876 905,898 C930,920 948,945 960,960 Z"/>
  </svg>

  <div class="brand">
    <div class="brand-name">tarrow.</div>
    <div class="brand-tagline">Tarrow Guidance Alliance</div>
  </div>

  <h1 class="event-title">
    <span class="title-red">Tarrow Flow &amp;</span>
    <span class="title-orange">Hum Unwind</span>
    <span class="title-red">Session -</span>
    <span class="title-ink">Bayline Mix</span>
  </h1>

  <div class="event-when">
    <div class="event-when-label">Event Date &amp; Time:</div>
    <div class="brush brush-day">WEDNESDAY,</div><br>
    <div class="brush brush-date">APRIL 20 | 7P - 9P</div>
  </div>

  <div class="event-where">
    <div class="event-where-label">Event Location:</div>
    <div class="event-where-venue">Reedhall at Cobbleyard</div>
  </div>
</main>
</body>
</html>
```